WP website design for Dorrance

We need a wordpress design that will incorporate a professional color scheme with company logo in a clean layout. The design needs to consider that this will be developed on a responsive theme. Colors are will be the green of the logo and any others that will creatively highlight it.

Industry/Entity Type

It Company

Font styles to use
Sans Serif

Requirements
Must have
• Navigation: 1) Home 2) Auctions 3) Auction Services 4) Sellers 5) KT Dorrance Livestock 6) About Us 7) Contact Us
Site will have slideshow element, image attached.
Widgets will be: 1)Email Signup form 2) Featured Auctions widget 3) Social Media (FB, Youtube, RSS) 4) News & Events blog
Footer will have smaller company logo, association logos (attached) and contact info (below)
▪ K.T. Dorrance Inc. / Auctioneers
▪ 4715 NC Hwy 91
▪ Belmora, NC 27640
▪ Office: (252) 555-0187
▪ Cell: (252) 555-0163
▪ email: ktdorrance@ktdorrance-example.com
Nice to have
• Site will have drop-down menus - please indicate the styling, for instance the dropdown menus

```html
<!DOCTYPE html>
<html lang="en">
<head>
<meta charset="utf-8">
<title>K.T. Dorrance Inc. / Auctioneers</title>
<link href="https://fonts.googleapis.com/css2?family=Arimo:ital,wght@0,400;0,700;1,400&family=Tinos:ital,wght@0,400;0,700;1,400&family=PT+Sans:wght@400;700&display=swap" rel="stylesheet">
<style>
:root{
  --green:#2f8a1c;
  --green-dark:#1f6b12;
  --ink:#222;
  --orange:#e39a1e;
  --page:#efefef;
  --nav:#3a3a3a;
  --footer:#333;
  --white:#fff;
  --line:#d6d6d6;
}
*{margin:0;padding:0;box-sizing:border-box}
html,body{width:834px;height:1200px;overflow:hidden}
body{background:var(--page);font-family:"Arimo",Arial,sans-serif;color:var(--ink);position:relative}

.site-header{position:absolute;left:0;top:0;width:834px;height:102px;background:var(--white)}
.brand{position:absolute;left:78px;top:26px;display:flex;align-items:center;gap:8px}
.brand-dot{width:34px;height:34px;border-radius:50%;background:var(--green)}
.brand-name{font-family:"Tinos",serif;font-size:19px;color:var(--green);line-height:1.1}
.social{position:absolute;left:482px;top:32px;display:flex;align-items:center;gap:8px}
.social-label{font-family:"Tinos",serif;font-style:italic;font-size:20px;color:var(--green);margin-right:6px}
.social-btn{width:32px;height:32px;border-radius:50%}

.main-nav{position:absolute;left:0;top:102px;width:834px;height:36px;background:var(--nav);display:flex;align-items:center;padding-left:64px}
.main-nav a{font-family:"PT Sans",sans-serif;font-size:11.5px;letter-spacing:.8px;color:var(--white);text-decoration:none;padding:0 15px;line-height:20px;border-right:1px solid #555}
.main-nav a:last-child{border-right:0}

.hero-band{position:absolute;left:0;top:138px}
.hero{position:absolute;left:70px;top:141px;width:693px;height:272px;clip-path:path("M0 0H693V227Q560 275 330 272L0 272Z")}
.hero-slide{position:absolute;left:0;top:0;width:470px;height:272px;background:linear-gradient(180deg,#c9d6e0 0%,#b89a6a 38%,#c88a3a 52%,#a5a59a 60%,#8a8474 100%)}
.signup{position:absolute;left:470px;top:0;width:223px;height:272px;background:linear-gradient(180deg,#f6f7f3 0%,#eceee6 60%,#dcdcd2 100%);padding:23px 22px}
.signup h2{font-family:"Tinos",serif;font-style:italic;font-weight:400;font-size:23px;color:var(--green);margin-left:2px}
.signup p{font-size:8.4px;line-height:11px;color:#333;margin:6px 0 12px;text-align:justify}
.signup .field{width:179px;height:25px;border:1px solid #bbb;background:var(--white);font-size:9px;color:#777;padding:0 6px;line-height:23px;margin-bottom:17px}
.signup .btn{display:inline-block;margin-top:6px;margin-left:2px;width:107px;height:27px;border:2px solid var(--green);border-radius:6px;background:linear-gradient(#3b9d26,#23760f);color:var(--white);font-family:"PT Sans",sans-serif;font-weight:700;font-size:12px;text-align:center;line-height:23px;box-shadow:0 0 0 1px #fff inset}

.welcome{position:absolute;left:72px;top:458px;width:425px}
.welcome h1{font-family:"Tinos",serif;font-weight:400;font-size:24px;color:var(--green)}
.welcome p{font-size:9.2px;line-height:14px;color:#222;margin-top:6px}

.auction-card{position:absolute;left:72px;width:440px;height:161px;background:var(--white);border:1px solid var(--line);border-radius:5px}
.auction-card h3{position:absolute;left:11px;top:13px;font-size:10.5px;letter-spacing:.7px;font-weight:700;color:#222;white-space:nowrap}
.auction-photo{position:absolute;left:11px;top:38px;width:153px;height:77px;background:linear-gradient(180deg,#8fb6dc 0%,#c9b79a 45%,#8c6e4e 70%,#5f8c3a 100%)}
.auction-info{position:absolute;left:176px;top:44px;width:255px;font-size:8.4px;font-style:italic;line-height:12.5px;color:#222}
.auction-info .kind{font-style:normal;font-weight:700;font-size:9.6px;color:var(--green);letter-spacing:.3px;margin-bottom:5px}
.auction-info .key{color:var(--orange)}
.auction-info .row{margin-bottom:6px}
.auction-info .tail{margin-top:6px}
.card-btn{position:absolute;top:124px;height:23px;width:71px;display:flex;align-items:center;justify-content:center;gap:5px;font-family:"Tinos",serif;font-weight:700;font-size:12px;color:var(--white)}
.card-btn.details{left:11px;background:#2b2b2b}
.card-btn.gallery{left:93px;background:var(--green)}
.card-btn .ico{width:11px;height:11px;border-radius:50%;background:#f2b21f}
.card-btn.gallery .ico{border-radius:2px}

.sidebar{position:absolute;left:550px;top:454px;width:204px;height:551px;background:var(--white);border:1px solid var(--line);border-radius:5px}
.widget-title{position:absolute;font-family:"Tinos",serif;font-style:italic;font-weight:400;font-size:20px;color:var(--green);white-space:nowrap}
.feat-link{position:absolute;left:17px;top:49px;font-size:8.2px;letter-spacing:.6px;color:var(--green);text-decoration:underline}
.feat-photo{position:absolute;left:16px;top:68px;width:150px;height:54px;border:2px solid #ddd;background:linear-gradient(180deg,#9cc3e8 0%,#d8c3a6 50%,#6e9a3c 100%)}
.feat-text{position:absolute;left:18px;top:128px;width:160px;font-size:8.2px;line-height:10px}
.read-more{position:absolute;left:18px;top:170px;width:51px;height:13px;border-radius:4px;background:#2d2d4a;color:var(--white);font-size:7.6px;font-style:italic;text-align:center;line-height:13px}
.news-item{position:absolute;left:12px;width:186px}
.news-thumb{position:absolute;left:0;top:0;width:50px;height:35px;background:linear-gradient(180deg,#8fb6dc,#c9b79a 55%,#5f8c3a)}
.news-date{position:absolute;left:57px;top:0;font-size:8.2px;color:var(--green)}
.news-text{position:absolute;left:58px;top:12px;width:128px;font-size:7.6px;line-height:10.5px;color:#333}
.quote{position:absolute;left:21px;top:403px;width:172px;font-size:8.2px;font-style:italic;line-height:15.3px;color:#222}
.qmark{position:absolute;font-family:"Tinos",serif;font-size:20px;font-weight:700;color:#222}

.site-footer{position:absolute;left:0;top:1119px;width:834px;height:81px;background:var(--footer)}
.contact{position:absolute;left:72px;top:11px;font-size:9.4px;line-height:14px;color:var(--white);font-style:normal}
.badge{position:absolute;background:#cfcfcf}
.foot-brand{position:absolute;left:668px;top:22px;display:flex;align-items:center;gap:6px}
.foot-brand .brand-dot{width:24px;height:24px;background:#cfcfcf}
.foot-brand .brand-name{color:#cfcfcf;font-size:14px}
</style>
</head>
<body>

<header class="site-header">
  <div class="brand">
    <span class="brand-dot"></span>
    <span class="brand-name">K.T. Dorrance<br>Inc. / Auctioneers</span>
  </div>
  <div class="social">
    <span class="social-label">Social Media:</span>
    <span class="social-btn" style="background:#1d4f7c" role="img" aria-label="Social network link"></span>
    <span class="social-btn" style="background:#2aa6e3" role="img" aria-label="Social network link"></span>
    <span class="social-btn" style="background:#f08c14" role="img" aria-label="News feed link"></span>
    <span class="social-btn" style="background:#8a8a8a" role="img" aria-label="Email link">
      <svg width="32" height="32" viewBox="0 0 32 32"><rect x="10" y="11" width="12" height="9" fill="none" stroke="#fff" stroke-width="1.3"/><path d="M10 11l6 5 6-5" fill="none" stroke="#fff" stroke-width="1.3"/></svg>
    </span>
  </div>
</header>

<nav class="main-nav">
  <a>HOME</a><a>AUCTIONS</a><a>AUCTION SERVICES</a><a>SELLERS</a><a>KT DORRANCE LIVESTOCK</a><a>ABOUT US</a><a>CONTACT US</a>
</nav>

<svg class="hero-band" width="834" height="300" viewBox="0 138 834 300">
  <path d="M0 138H834V370Q640 436 430 433Q200 428 0 358Z" fill="var(--green)"/>
</svg>
<div class="hero">
  <div class="hero-slide" role="img" aria-label="Slideshow photo: autumn trees and meadow reflected in a still pond"></div>
  <section class="signup">
    <h2>Email Sign Up</h2>
    <p>Lorem ipsum dolor sit amet, consectetuer adipiscing elit. Nam</p>
    <div class="field">Your Name</div>
    <div class="field">Your Name</div>
    <span class="btn">Subscribe Now</span>
  </section>
</div>

<section class="welcome">
  <h1>Welcome To Dorrance Auctioneers</h1>
  <p>Lorem ipsum dolor sit amet, consectetur adipisicing elit, sed do eiusmod tempor incididunt ut labore et dolore magna aliqua. Ut enim ad minim veniam, quis nostrud exercitation ullamco laboris nisi ut aliquipin voluptate velit esse cillum dolore eu fugiat nulla pariatur.</p>
</section>

<article class="auction-card" style="top:558px">
  <h3>2005 SUMMIT TEXT OF THE PRINTING AND CREST 34-FT. CAMPER</h3>
  <div class="auction-photo" role="img" aria-label="Photo of a two-storey house with lawn"></div>
  <div class="auction-info">
    <div class="kind">LIVE ON-SITE AUCTION</div>
    <div class="row"><span class="key">Begins:</span>&nbsp; Tuesday, April 23, 2013 at 10:00 AM EDT</div>
    <div class="row"><span class="key">Location:</span>&nbsp; Cedar Pond Entrance- 1180 S. Ridge Hwy 14 text of the printing and typesetting industry. Lorem Ipsum has been the industry's standard dummy text ever since the 1500s,</div>
    <div class="tail">Cedar Pond Rd (Auction Property) Lake Ipsum has been the industry's standard dummy text ever Larkfield, FL 33999</div>
  </div>
  <span class="card-btn details"><span class="ico"></span>Details</span>
  <span class="card-btn gallery"><span class="ico"></span>Gallery</span>
</article>

<article class="auction-card" style="top:751px">
  <h3>2005 SUMMIT TEXT OF THE PRINTING AND CREST 34-FT. CAMPER</h3>
  <div class="auction-photo" role="img" aria-label="Photo of a two-storey house with lawn"></div>
  <div class="auction-info">
    <div class="kind">LIVE ON-SITE AUCTION</div>
    <div class="row"><span class="key">Begins:</span>&nbsp; Tuesday, April 23, 2013 at 10:00 AM EDT</div>
    <div class="row"><span class="key">Location:</span>&nbsp; Cedar Pond Entrance- 1180 S. Ridge Hwy 14 text of the printing and typesetting industry. Lorem Ipsum has been the industry's standard dummy text ever since the 1500s,</div>
    <div class="tail">Cedar Pond Rd (Auction Property) Lake Ipsum has been the industry's standard dummy text ever Larkfield, FL 33999</div>
  </div>
  <span class="card-btn details"><span class="ico"></span>Details</span>
  <span class="card-btn gallery"><span class="ico"></span>Gallery</span>
</article>

<article class="auction-card" style="top:934px">
  <h3>2005 SUMMIT TEXT OF THE PRINTING AND CREST 34-FT. CAMPER</h3>
  <div class="auction-photo" role="img" aria-label="Photo of a two-storey house with lawn"></div>
  <div class="auction-info">
    <div class="kind">LIVE ON-SITE AUCTION</div>
    <div class="row"><span class="key">Begins:</span>&nbsp; Tuesday, April 23, 2013 at 10:00 AM EDT</div>
    <div class="row"><span class="key">Location:</span>&nbsp; Cedar Pond Entrance- 1180 S. Ridge Hwy 14 text of the printing and typesetting industry. Lorem Ipsum has been the industry's standard dummy text ever since the 1500s,</div>
    <div class="tail">Cedar Pond Rd (Auction Property) Lake Ipsum has been the industry's standard dummy text ever Larkfield, FL 33999</div>
  </div>
  <span class="card-btn details"><span class="ico"></span>Details</span>
  <span class="card-btn gallery"><span class="ico"></span>Gallery</span>
</article>

<aside class="sidebar">
  <h2 class="widget-title" style="left:15px;top:12px">Featured Auctions</h2>
  <span class="feat-link">TRACTOR * HI LIFT * MACHINERY</span>
  <div class="feat-photo" role="img" aria-label="Photo of an estate house among palm trees"></div>
  <p class="feat-text"><b>Saturday</b> March 16, 2013 at 10:00 AM simply dummy text of the printing and typesetting industry.</p>
  <span class="read-more">read more</span>

  <h2 class="widget-title" style="left:10px;top:210px">News &amp; Events</h2>
  <div class="news-item" style="top:243px">
    <div class="news-thumb" role="img" aria-label="Photo of a house"></div>
    <span class="news-date">SETURDAY MARCH 6, 2014</span>
    <p class="news-text">Lorem is that it has a more-or-less normal distribution of letters,</p>
  </div>
  <div class="news-item" style="top:297px">
    <div class="news-thumb" role="img" aria-label="Photo of a house"></div>
    <span class="news-date">SETURDAY MARCH 6, 2014</span>
    <p class="news-text">Lorem is that it has a more-or-less normal distribution of letters,</p>
  </div>

  <h2 class="widget-title" style="left:10px;top:371px">Testimonials</h2>
  <span class="qmark" style="left:16px;top:396px">&ldquo;</span>
  <p class="quote">&nbsp;&nbsp;&nbsp;&nbsp;Lorem ipsum dolor sit amet, consecte-tur adipisicing elit, sed do eiusmod tempor incididunt ut labore et dolore magna aliqua. Ut enim ad minim veniam, quis nostrud exercitation ullamco laboris teur sint occae-cat cupidatat non proident, sunt in culpa qui officia deserunt mollit</p>
  <span class="qmark" style="left:108px;top:498px">&rdquo;</span>
</aside>

<footer class="site-footer">
  <address class="contact">
    K.T. Dorrance Inc. / Auctioneers<br>
    4715 NC Hwy 91 Belmora, NC 27640<br>
    Office: (252) 555-0187 , Cell: (252) 555-0163<br>
    email: ktdorrance@ktdorrance-example.com
  </address>
  <span class="badge" style="left:502px;top:26px;width:50px;height:22px;border-radius:3px" role="img" aria-label="Association badge"></span>
  <span class="badge" style="left:560px;top:24px;width:34px;height:26px;border-radius:4px" role="img" aria-label="Association badge"></span>
  <span class="badge" style="left:605px;top:20px;width:34px;height:34px;border-radius:50%" role="img" aria-label="Association badge"></span>
  <div class="foot-brand">
    <span class="brand-dot"></span>
    <span class="brand-name">K.T. Dorrance<br>Inc. / Auctioneers</span>
  </div>
</footer>

</body>
</html>
```